Creative Web Site to Sell Geology Classes for Homeschooling

I am starting a business to sell a variety of geology classes for homeschoolers. I am targeting classes for kids with dyslexia, although others will benefit as well. The classes will be delivered by mail. Each class will have a video, a manual, and rock samples. I need a landing page that I can link over to seven other pages, a page with a template for products, and a template of the pages that will not have products. All should be easy to edit. All pages should display well with handheld devices (phones), as well as desktops.

Designs look the same

```html
<!DOCTYPE html>
<html lang="en">
<head>
<meta charset="utf-8">
<title>Pebble Path Academy — Geology Classes for Homeschoolers</title>
<link rel="stylesheet" href="https://fonts.googleapis.com/css2?family=Montserrat:ital,wght@0,400;0,500;0,600;0,700;1,400&display=swap">
<style>
:root{
  --coral:#fa6b5e;
  --coral-soft:#fd8a7d;
  --teal:#5fd1bf;
  --yellow:#f8c95a;
  --purple:#5a5680;
  --ink:#2a2a2a;
  --text:#8a8a8a;
  --muted:#a3a3a3;
  --white:#ffffff;
  --band:#f6f6f6;
  --band-light:#fafafa;
  --footer-strip:#f3f3f3;
}
*{box-sizing:border-box;margin:0;padding:0}
html,body{width:1200px;height:3416px;overflow:hidden}
body{font-family:"Montserrat",sans-serif;color:var(--ink);background:var(--white);position:relative}
.dot{color:var(--coral)}
.btn{display:inline-flex;align-items:center;justify-content:center;width:228px;height:56px;background:var(--coral);color:var(--white);font-size:14px;font-weight:500;letter-spacing:.5px;text-transform:uppercase;text-decoration:none;border-radius:3px;box-shadow:0 6px 14px rgba(250,107,94,.3)}
.section-title{font-size:36px;font-weight:700;text-align:center}
.section-sub{font-size:15px;color:var(--muted);text-align:center;margin-top:18px}

/* Header */
.site-header{position:absolute;top:0;left:0;width:1200px;height:80px;display:flex;align-items:center;justify-content:space-between;padding:0 122px 0 125px;background:var(--white)}
.brand{display:flex;align-items:center;gap:10px;font-weight:700;font-size:20px;color:var(--coral);text-decoration:none;white-space:nowrap}
.brand-mark{width:40px;height:40px;border-radius:50%;background:var(--coral);flex:none}
.main-nav{display:flex;gap:0}
.main-nav a{font-size:14px;color:var(--ink);text-decoration:none;width:112px;text-align:center;white-space:nowrap}
.main-nav a:last-child{width:auto;margin-left:10px}

/* Hero */
.hero{position:absolute;top:80px;left:0;width:1200px;height:507px}
.hero-photo{position:absolute;inset:0;background:linear-gradient(100deg,#6f6a86 0%,#8d8699 35%,#c4b8b4 65%,#e3ddd8 100%)}
.hero-content{position:absolute;left:122px;top:118px;color:var(--white)}
.hero-title{font-size:44px;font-weight:700;line-height:1.02}
.hero-sub{font-size:17px;margin-top:20px}
.hero .btn{margin-top:48px}

/* Help */
.help{position:absolute;top:587px;left:0;width:1200px;height:464px;padding-top:88px}
.help-grid{display:flex;gap:15px;margin:56px 0 0 122px}
.help-card{width:229px;height:166px;border:3px solid;border-radius:6px;display:flex;align-items:center;justify-content:center;text-align:center;padding:0 18px;font-size:17px;font-weight:600;line-height:1.6;box-shadow:0 8px 18px rgba(0,0,0,.08)}
.help-card.coral{border-color:var(--coral)}
.help-card.teal{border-color:var(--teal)}
.help-card.yellow{border-color:var(--yellow)}
.help-card.purple{border-color:var(--purple)}

/* About */
.about{position:absolute;top:1051px;left:0;width:1200px;height:527px;background:var(--band)}
.about-photo{position:absolute;left:122px;top:87px;width:390px;height:352px;border-radius:6px;background:linear-gradient(135deg,#d8cfc2 0%,#c0a88c 45%,#e4ddd2 100%);box-shadow:0 10px 22px rgba(0,0,0,.12)}
.about-body{position:absolute;left:608px;top:104px;width:470px}
.about-title{font-size:36px;font-weight:700}
.about-body p{font-size:14.5px;color:var(--text);line-height:1.65;margin-top:18px}
.about-body p+p{margin-top:22px}
.about .btn{margin-top:40px}

/* Classes */
.classes{position:absolute;top:1578px;left:0;width:1200px;height:714px;padding-top:52px}
.class-grid{display:flex;gap:16px;margin:46px 0 0 122px}
.class-card{width:308px;height:400px;background:var(--white);border-radius:4px;box-shadow:0 6px 20px rgba(0,0,0,.1);padding:16px 16px 0}
.class-photo{height:135px;border-radius:4px}
.class-photo.one{background:linear-gradient(135deg,#7a4a3a,#c79a82)}
.class-photo.two{background:linear-gradient(135deg,#9c7a78,#e2cfc9)}
.class-photo.three{background:linear-gradient(135deg,#c96a6e,#e7ddd8)}
.class-card h3{font-size:15.5px;font-weight:600;margin-top:38px}
.class-card p{font-size:13.5px;color:var(--text);line-height:1.6;margin-top:14px}
.learn-more{display:block;margin-top:36px;font-size:12.5px;font-weight:600;color:var(--coral);text-decoration:none;text-transform:uppercase}
.classes .btn{position:absolute;left:486px;top:614px}

/* Testimonials */
.testimonials{position:absolute;top:2292px;left:0;width:1200px;height:528px;background:var(--band-light);padding-top:38px}
.quote-grid{display:flex;margin:48px 0 0 122px}
.quote{width:320px;text-align:center}
.avatar{width:148px;height:148px;border-radius:50%;margin:0 auto}
.avatar.a1{background:radial-gradient(circle at 50% 40%,#7a4a35,#4b3b4a)}
.avatar.a2{background:radial-gradient(circle at 50% 40%,#e0bfa8,#3a3a3a)}
.avatar.a3{background:radial-gradient(circle at 50% 40%,#c89a86,#5a2430)}
.quote p{font-size:13.5px;font-style:italic;color:var(--text);line-height:1.7;margin:16px auto 0;width:280px}
.quote cite{display:block;font-style:normal;font-size:13.5px;font-weight:600;color:var(--coral);margin-top:22px}

/* Subscribe */
.subscribe{position:absolute;top:2820px;left:0;width:1200px;height:388px;display:flex}
.subscribe-photo{width:600px;height:100%;background:linear-gradient(110deg,#8b9a58 0%,#cdbfb0 45%,#ece6e0 100%)}
.subscribe-panel{width:600px;height:100%;background:var(--coral-soft);text-align:center;padding-top:40px;color:var(--white)}
.subscribe-title{font-size:36px;font-weight:700}
.subscribe-sub{font-size:15px;margin-top:14px}
.subscribe-form{display:flex;flex-direction:column;align-items:center;margin-top:16px}
.field{width:390px;height:56px;border:none;border-radius:3px;background:var(--white);font-family:inherit;font-size:15px;color:var(--muted);text-align:center;margin-bottom:19px}
.subscribe-btn{width:229px;height:56px;border:2px solid var(--white);background:transparent;color:var(--white);font-family:inherit;font-size:14px;font-weight:500;text-transform:uppercase;border-radius:3px;margin-top:6px}

/* Footer */
.site-footer{position:absolute;top:3208px;left:0;width:1200px;height:127px}
.site-footer .brand{position:absolute;left:125px;top:43px}
.footer-links{position:absolute;left:445px;top:0;height:127px;display:flex;align-items:center;gap:32px}
.footer-links a{font-size:13px;color:var(--ink);text-decoration:none;white-space:nowrap}
.social{position:absolute;left:867px;top:43px;display:flex;gap:16px}
.social span{width:40px;height:40px;border-radius:50%;background:var(--purple)}
.copyright{position:absolute;top:3335px;left:0;width:1200px;height:81px;background:var(--footer-strip);display:flex;align-items:center;justify-content:center;font-size:13px;color:var(--ink);white-space:nowrap}
.copyright span{color:var(--coral);margin-left:4px}
</style>
</head>
<body>

<header class="site-header">
  <a class="brand" href="#"><span class="brand-mark"></span>Pebble Path Academy</a>
  <nav class="main-nav">
    <a href="#">Home</a><a href="#">Classes</a><a href="#">About us</a><a href="#">Blog</a><a href="#">Contact</a>
  </nav>
</header>

<section class="hero">
  <div class="hero-photo" role="img" aria-label="Photo of a father helping his daughter draw at a desk"></div>
  <div class="hero-content">
    <h1 class="hero-title">Get the Best<br>online classes for<br>you and your child<span class="dot">.</span></h1>
    <p class="hero-sub">A variety of geology classes for homeschoolers</p>
    <a class="btn" href="#">See our courses</a>
  </div>
</section>

<section class="help">
  <h2 class="section-title">How can we help<span class="dot">.</span></h2>
  <p class="section-sub">A variety of geology classes for homeschoolers</p>
  <div class="help-grid">
    <div class="help-card coral">Could it be<br>dyslexia?</div>
    <div class="help-card teal">Can parents<br>teach their kids<br>with dyslexia?</div>
    <div class="help-card yellow">How to teach<br>kids with dyslexia?</div>
    <div class="help-card purple">What kinds of<br>teaching materials<br>should I use?</div>
  </div>
</section>

<section class="about">
  <div class="about-photo" role="img" aria-label="Photo of a family giving each other a high five at the kitchen table"></div>
  <div class="about-body">
    <h2 class="about-title">We are Pebble Path<span class="dot">.</span></h2>
    <p>Lorem ipsum dolor sit amet, consectetur adipiscing elit. Vivamus at sagittis erat, sed efficitur lectus. Nullam leo sapien, vehicula nec facilisis ac, cursus ac justo.</p>
    <p>Aenean finibus quam dolor, eu lobortis massa scelerisque ut. Cras maximus nisi quis felis egestas sodales. Vestibulum enim lectus, tempor condimentum orci sed, aliquet consectetur massa.</p>
    <a class="btn" href="#">See our courses</a>
  </div>
</section>

<section class="classes">
  <h2 class="section-title">Our Classes<span class="dot">.</span></h2>
  <p class="section-sub">A variety of geology classes for homeschoolers</p>
  <div class="class-grid">
    <article class="class-card">
      <div class="class-photo one" role="img" aria-label="Photo of a mother reading with her son"></div>
      <h3>Teach Them How They Learn</h3>
      <p>Lorem ipsum dolor sit amet, consectetur adipiscing elit. Vivamus at sagittis erat, sed efficitur lectus. Nullam leo sapien, vehicula nec facilisis ac.</p>
      <a class="learn-more" href="#">Learn more</a>
    </article>
    <article class="class-card">
      <div class="class-photo two" role="img" aria-label="Photo of a parent and child studying a book together"></div>
      <h3>Reading Instruction That Works</h3>
      <p>Lorem ipsum dolor sit amet, consectetur adipiscing elit. Vivamus at sagittis erat, sed efficitur lectus. Nullam leo sapien, vehicula nec facilisis ac.</p>
      <a class="learn-more" href="#">Learn more</a>
    </article>
    <article class="class-card">
      <div class="class-photo three" role="img" aria-label="Photo of a girl writing at a table with her mother"></div>
      <h3>Fluency and Comprehension</h3>
      <p>Lorem ipsum dolor sit amet, consectetur adipiscing elit. Vivamus at sagittis erat, sed efficitur lectus. Nullam leo sapien, vehicula nec facilisis ac.</p>
      <a class="learn-more" href="#">Learn more</a>
    </article>
  </div>
  <a class="btn" href="#">See more courses</a>
</section>

<section class="testimonials">
  <h2 class="section-title">Testimonials<span class="dot">.</span></h2>
  <div class="quote-grid">
    <figure class="quote">
      <div class="avatar a1" role="img" aria-label="Portrait of Nora Wells"></div>
      <p>Lorem ipsum dolor sit amet, consectetur adipiscing elit. Vivamus at sagittis erat, sed efficitur lectus. Nullam leo sapien, vehicula nec facilisis ac, cursus ac justo.</p>
      <cite>Nora Wells</cite>
    </figure>
    <figure class="quote">
      <div class="avatar a2" role="img" aria-label="Portrait of Liam Carter"></div>
      <p>Lorem ipsum dolor sit amet, consectetur adipiscing elit. Vivamus at sagittis erat, sed efficitur lectus. Nullam leo sapien, vehicula nec facilisis ac, cursus ac justo.</p>
      <cite>Liam Carter</cite>
    </figure>
    <figure class="quote">
      <div class="avatar a3" role="img" aria-label="Portrait of Mateo Ruiz"></div>
      <p>Lorem ipsum dolor sit amet, consectetur adipiscing elit. Vivamus at sagittis erat, sed efficitur lectus. Nullam leo sapien, vehicula nec facilisis ac, cursus ac justo.</p>
      <cite>Mateo Ruiz</cite>
    </figure>
  </div>
</section>

<section class="subscribe">
  <div class="subscribe-photo" role="img" aria-label="Photo of a father and daughter cheering with their arms raised"></div>
  <div class="subscribe-panel">
    <h2 class="subscribe-title">Subscribe.</h2>
    <p class="subscribe-sub">A variety of geology classes for homeschoolers</p>
    <form class="subscribe-form">
      <input class="field" type="text" placeholder="Full Name">
      <input class="field" type="email" placeholder="Email">
      <button class="subscribe-btn" type="button">Subscribe now!</button>
    </form>
  </div>
</section>

<footer class="site-footer">
  <a class="brand" href="#"><span class="brand-mark"></span>Pebble Path Academy</a>
  <nav class="footer-links">
    <a href="#">Privacy Policy</a><a href="#">Terms &amp; Conditions</a><a href="#">FAQs</a>
  </nav>
  <div class="social" aria-label="Social links">
    <span role="img" aria-label="Social link"></span>
    <span role="img" aria-label="Social link"></span>
    <span role="img" aria-label="Social link"></span>
    <span role="img" aria-label="Social link"></span>
  </div>
</footer>
<div class="copyright">© Copyright 2019 <span>Pebble Path Academy</span></div>

</body>
</html>
```